Bref créative
Stationary and Business Cards Orla Ridge Capital
Stationary, Envelopes, Business Cards
Professional
Marcus Bellwin
Managing Partner
8734 Fernhollow Ave. Suite 4580
Los Angeles, CA 90217
marcus@orlaridgecapital.example
orlaridgecapital.example
Design should be similar to the informational side of the business card (with bull silhouette) I had designed previously (uploaded), but with colors matching my website colors of black+white+blue (see previous contest and also uploaded).
Should contain the following:
-Company Logo (uploaded)
-The Slogan "Hedge Fund Strategies at Mutual Fund Prices"
-And the offer "Free Financial Check-Up"
Here is the previous business card. I don't care about the pattern in the background as that didn't show up in printing anyway.
here is a draft version of the website, to give you an idea of the general appearance
here is the company logo

```html
<!DOCTYPE html>
<html lang="en">
<head>
<meta charset="utf-8">
<title>Orla Ridge Capital — Stationery Set</title>
<link href="https://fonts.googleapis.com/css2?family=Cinzel:wght@600&family=Lato:wght@400;700&display=swap" rel="stylesheet">
<style>
  :root {
    --ink: #111316;
    --charcoal: #24282c;
    --teal: #1d8fb0;
    --teal-deep: #0f5f7a;
    --teal-light: #5fc2de;
    --paper: #ffffff;
    --mist: #eef1f3;
    --stage: #d8d6d2;
    --grey-text: #55595e;
  }
  * { box-sizing: border-box; margin: 0; padding: 0; }
  html, body { width: 1200px; height: 1091px; overflow: hidden; }
  body { background: var(--stage); font-family: "Lato", sans-serif; color: var(--ink); position: relative; }

  .piece { position: absolute; background: var(--paper); box-shadow: 0 3px 10px rgba(0,0,0,.25); overflow: hidden; }

  /* brand lockup */
  .brand { display: flex; align-items: center; gap: 6px; }
  .brand-mark { width: 14px; height: 14px; background: var(--teal); flex: none; }
  .brand-name { font-family: "Cinzel", serif; font-weight: 600; color: var(--teal-deep); letter-spacing: 2px; }
  .brand--light .brand-name { color: var(--paper); }

  .bull-art { background: linear-gradient(135deg, #2b2f33, #0d0f11); border-radius: 2px; }
  .bull-art--light { background: linear-gradient(135deg, #cfe6ee, #9bc7d6); }

  /* business cards */
  .card { width: 198px; height: 112px; }
  .card-front .card-band { height: 42px; padding: 7px 10px; background: linear-gradient(90deg, var(--teal-deep), var(--teal)); color: var(--paper); }
  .card-front--dark .card-band { background: linear-gradient(90deg, var(--ink), var(--charcoal)); }
  .card-front--plain .card-band { background: var(--paper); color: var(--ink); border-bottom: 2px solid var(--teal); }
  .card-name { font-size: 11px; font-weight: 700; }
  .card-title { font-size: 7px; opacity: .85; margin-top: 2px; }
  .card-front .brand { margin: 16px 0 0 12px; }
  .card-front .brand-name { font-size: 15px; }
  .card-contact { position: absolute; left: 12px; bottom: 6px; font-size: 5px; color: var(--grey-text); line-height: 1.4; }

  .card-back { padding: 10px 12px; }
  .card-back--dark { background: var(--ink); color: var(--paper); }
  .card-back--teal { background: linear-gradient(180deg, var(--teal), var(--teal-deep)); color: var(--paper); }
  .card-back--plain { background: var(--mist); color: var(--ink); }
  .slogan { font-size: 7.5px; }
  .card-back .bull-art { position: absolute; left: 60px; top: 34px; width: 78px; height: 42px; }
  .offer { position: absolute; right: 12px; bottom: 9px; font-size: 8px; }
  .offer strong { font-size: 10px; }

  /* envelope */
  .envelope { left: 90px; top: 555px; width: 480px; height: 180px; }
  .envelope-flap { position: absolute; inset: 0; }
  .envelope-band { position: absolute; left: 0; top: 78px; width: 100%; height: 36px; background: linear-gradient(90deg, var(--ink), var(--charcoal)); border-bottom: 3px solid var(--teal); padding: 8px 14px; }
  .envelope-band .brand-name { font-size: 16px; }
  .envelope-return { position: absolute; left: 14px; bottom: 14px; font-size: 6px; color: var(--grey-text); }

  /* compliment slip */
  .slip { left: 90px; top: 750px; width: 480px; height: 300px; }
  .slip-head { height: 50px; border-bottom: 3px solid var(--teal); padding: 14px 16px; }
  .slip-head .brand-name { font-size: 17px; }
  .slip-address { margin: 14px 16px; font-size: 7px; color: var(--grey-text); line-height: 1.5; }
  .slip-foot { position: absolute; bottom: 0; left: 0; width: 100%; height: 20px; background: var(--ink); color: var(--paper); font-size: 7px; text-align: center; line-height: 20px; letter-spacing: 1px; }

  /* letterhead */
  .letterhead { left: 615px; top: 555px; width: 540px; height: 510px; }
  .letter-head { height: 56px; background: linear-gradient(90deg, var(--ink), var(--charcoal)); border-bottom: 4px solid var(--teal); padding: 14px 20px; }
  .letter-head .brand-name { font-size: 22px; }
  .letter-head .brand-mark { width: 22px; height: 22px; }
  .letter-body { padding: 26px 36px 0; font-size: 7.5px; line-height: 1.6; color: var(--charcoal); }
  .letter-body p { margin-bottom: 10px; }
  .letter-foot { position: absolute; bottom: 0; left: 0; width: 100%; }
  .letter-contact { font-size: 6.5px; text-align: center; color: var(--grey-text); padding: 6px 0; border-top: 1px solid var(--teal); margin: 0 24px; }
  .letter-web { height: 18px; background: var(--ink); color: var(--paper); font-size: 7px; text-align: center; line-height: 18px; letter-spacing: 1px; }
</style>
</head>
<body>

<!-- business card fronts -->
<div class="piece card card-front" style="left:189px;top:45px">
  <div class="card-band"><div class="card-name">Marcus Bellwin</div><div class="card-title">Managing Partner</div></div>
  <div class="brand"><span class="brand-mark"></span><span class="brand-name">BELLWIN</span></div>
  <div class="card-contact">8734 Fernhollow Ave. Suite 4580 · Los Angeles, CA 90217<br>marcus@orlaridgecapital.example · (310) 555-0148</div>
</div>
<div class="piece card card-front card-front--dark" style="left:405px;top:45px">
  <div class="card-band"><div class="card-name">Marcus Bellwin</div><div class="card-title">Managing Partner</div></div>
  <div class="brand"><span class="brand-mark"></span><span class="brand-name">BELLWIN</span></div>
  <div class="card-contact">8734 Fernhollow Ave. Suite 4580 · Los Angeles, CA 90217<br>marcus@orlaridgecapital.example · (310) 555-0148</div>
</div>
<div class="piece card card-front card-front--plain" style="left:624px;top:45px">
  <div class="card-band"><div class="card-name">Marcus Bellwin</div><div class="card-title">Managing Partner</div></div>
  <div class="brand"><span class="brand-mark"></span><span class="brand-name">BELLWIN</span></div>
  <div class="card-contact">8734 Fernhollow Ave. Suite 4580 · Los Angeles, CA 90217<br>marcus@orlaridgecapital.example · (310) 555-0148</div>
</div>

<!-- business card backs -->
<div class="piece card card-back card-back--dark" style="left:189px;top:171px">
  <div class="slogan">Hedge Fund Strategies at Mutual Fund Prices</div>
  <div class="bull-art bull-art--light" role="img" aria-label="Charging bull silhouette"></div>
  <div class="offer">Free <strong>Financial</strong> Check-Up</div>
</div>
<div class="piece card card-back card-back--teal" style="left:405px;top:171px">
  <div class="slogan">Hedge Fund Strategies at Mutual Fund Prices</div>
  <div class="bull-art bull-art--light" role="img" aria-label="Charging bull silhouette"></div>
  <div class="offer">Free <strong>Financial</strong> Check-Up</div>
</div>
<div class="piece card card-back card-back--plain" style="left:624px;top:171px">
  <div class="slogan">Hedge Fund Strategies at Mutual Fund Prices</div>
  <div class="bull-art" role="img" aria-label="Charging bull silhouette"></div>
  <div class="offer">Free <strong>Financial</strong> Check-Up</div>
</div>

<!-- envelope -->
<div class="piece envelope">
  <svg class="envelope-flap" viewBox="0 0 480 180" preserveAspectRatio="none">
    <polyline points="0,0 240,78 480,0" fill="none" stroke="#d5dadd" stroke-width="1.5"/>
  </svg>
  <div class="envelope-band"><div class="brand brand--light"><span class="brand-mark"></span><span class="brand-name">BELLWIN</span></div></div>
  <div class="envelope-return">8734 Fernhollow Ave. Suite 4580 · Los Angeles, CA 90217 · (310) 555-0148 · marcus@orlaridgecapital.example</div>
</div>

<!-- compliment slip -->
<div class="piece slip">
  <div class="slip-head"><div class="brand"><span class="brand-mark"></span><span class="brand-name">BELLWIN</span></div></div>
  <div class="slip-address">8734 Fernhollow Ave. Suite 4580<br>Los Angeles, CA 90217</div>
  <div class="slip-foot">orlaridgecapital.example</div>
</div>

<!-- letterhead -->
<div class="piece letterhead">
  <div class="letter-head"><div class="brand brand--light"><span class="brand-mark"></span><span class="brand-name">BELLWIN</span></div></div>
  <div class="letter-body">
    <p>Dear Client,</p>
    <p>Thank you for choosing our firm to guide your investments this year. Our team reviews every portfolio with care, balancing growth and protection so that your savings work steadily toward the goals that matter most to you and your family.</p>
    <p>We apply the disciplined methods of larger funds while keeping our fees close to those of common mutual funds. Each quarter you will receive a clear report on results, risk and the changes we recommend for the months ahead.</p>
    <p>Our advisors hold regular meetings to review market conditions and adjust each plan where needed. You can always expect honest advice and steady communication.</p>
    <p>Please reach out at any time to book your free financial check-up. We look forward to meeting with you soon.</p>
    <p>Sincerely,<br>Marcus Bellwin</p>
  </div>
  <div class="letter-foot">
    <div class="letter-contact">8734 Fernhollow Ave. Suite 4580 · Los Angeles, CA 90217 · (310) 555-0148 · marcus@orlaridgecapital.example</div>
    <div class="letter-web">orlaridgecapital.example</div>
  </div>
</div>

</body>
</html>
```